The Maple Sprout Clinic needs a Letterhead

We are a bilingual pediatric clinic located in Montreal, Canada.

Our english name is Maple Sprout Clinic
Our french name is Clinique du petit ruisseau

We offer complete care for children including general pediatric care, pediatric specialist care such as Ear, Nose and Throat, Urology, Neurology and Adolescent Medicine. We also have paramedical specialists such as psychologists, social workers, occupational therapists, speech and language pathologists.

The letterhead must use and be harmonious with our new logo. See Design #4923293. We need two types of letterhead. One for a the Logo and both english and french names on the top and the second with the list of current staff on the left. I have uploaded two old examples for you to see. Thanks and good luck.

Font styles to use
Sans Serif

Colors
3176b5
9d9d9d

Requirements
Must have
• Include our logo.
Nice to have
• Most of our printing is done in black and white. So a grayscale design is fine.
I have included a color and grayscale versions of our logo.

We prefer clean modern designs.

```html
<!DOCTYPE html>
<html lang="en">
<head>
<meta charset="utf-8">
<title>Maple Sprout Clinic – Letterhead</title>
<link href="https://fonts.googleapis.com/css2?family=Questrial&family=Arimo:wght@400&display=swap" rel="stylesheet">
<style>
  :root {
    --backdrop: #dedede;
    --paper: #f8f8f8;
    --brand-colour: #6a6cae;
    --brand-grey: #8c8c8c;
    --footer-text: #4a4a4a;
    --rule: #c4c4c4;
  }
  * { margin: 0; padding: 0; box-sizing: border-box; }
  html, body {
    width: 1200px; height: 800px; overflow: hidden;
    background: var(--backdrop);
  }
  .canvas { position: relative; width: 1200px; height: 800px; }
  .sheet {
    position: absolute; top: 111px;
    width: 410px; height: 575px;
    background: var(--paper);
  }
  .sheet--colour { left: 165px; --ink: var(--brand-colour); }
  .sheet--grey { left: 613px; --ink: var(--brand-grey); }

  .masthead {
    position: absolute; top: 26px; left: 0; right: 0;
    display: flex; justify-content: center; align-items: center; gap: 6px;
    font-family: "Questrial", sans-serif; font-size: 11px; line-height: 12px;
    color: var(--ink);
  }
  .masthead__fr { text-align: right; width: 62px; }
  .masthead__en { text-align: left; width: 62px; }
  .masthead__dot {
    width: 36px; height: 36px; border-radius: 50%;
    background: var(--ink);
  }

  .contact-bar {
    position: absolute; left: 29px; right: 30px; bottom: 18px;
    height: 16px;
    font-family: "Arimo", sans-serif; font-size: 6px; line-height: 7px;
    color: var(--footer-text);
  }
  .contact-bar__address { position: absolute; left: 0; top: 1px; }
  .contact-bar__tel { position: absolute; left: 181px; top: 5px; }
  .contact-bar__fax { position: absolute; left: 291px; top: 5px; }
  .contact-bar__rule {
    position: absolute; top: 0; width: 1px; height: 16px; background: var(--rule);
  }
  .contact-bar__rule--one { left: 122px; }
  .contact-bar__rule--two { left: 231px; }
</style>
</head>
<body>
<main class="canvas">
  <section class="sheet sheet--colour" aria-label="Letterhead, colour">
    <header class="masthead">
      <div class="masthead__fr">Clinique<br>du petit<br>ruisseau</div>
      <div class="masthead__dot"></div>
      <div class="masthead__en">Maple<br>Sprout<br>Clinic</div>
    </header>
    <footer class="contact-bar">
      <div class="contact-bar__address">2150 boul. des Érables, Suite 100,<br>Laval, Qc, H7A 2B3</div>
      <span class="contact-bar__rule contact-bar__rule--one"></span>
      <div class="contact-bar__tel">tél (514) 555-0142</div>
      <span class="contact-bar__rule contact-bar__rule--two"></span>
      <div class="contact-bar__fax">fax (514) 555-0199</div>
    </footer>
  </section>

  <section class="sheet sheet--grey" aria-label="Letterhead, greyscale">
    <header class="masthead">
      <div class="masthead__fr">Clinique<br>du petit<br>ruisseau</div>
      <div class="masthead__dot"></div>
      <div class="masthead__en">Maple<br>Sprout<br>Clinic</div>
    </header>
    <footer class="contact-bar">
      <div class="contact-bar__address">2150 boul. des Érables, Suite 100,<br>Laval, Qc, H7A 2B3</div>
      <span class="contact-bar__rule contact-bar__rule--one"></span>
      <div class="contact-bar__tel">tél (514) 555-0142</div>
      <span class="contact-bar__rule contact-bar__rule--two"></span>
      <div class="contact-bar__fax">fax (514) 555-0199</div>
    </footer>
  </section>
</main>
</body>
</html>
```